Business Card Design Project : Ferncliff Media

In preparation for market launch, Whistler's Ferncliff Media require the development of a business card. Ferncliff Media is a Community online publishing web portal. We provide the the city of Whistler located in B.C. (Canada) business directories, News, Classified ads, News, Events and blogs etc.

The main focus of the brand is to help local businesses to corporate with their online advertisement and marketing. Meeting our clients face to face is a must (B2B).

Target Market(s)

The target market is B2B customers. Business Owners to Marketing, advertising Managers

Industry/Entity Type

Business

Requirements
Must have
• - The business card will be two sided.
the BACK side will have our logo which consist of (icon, url,slogan) submited. The logo will be middle and centred.

The FRONT side should have company details:

Company Legal Name: TALLPINE FERNCLIFF MEDIA

Dale Morrow
Director of Sales & Marketing

www.tallpineferncliff.biz
dale@tallpineferncliff.biz

Phone: 604 555 0138
#2217 - 581 E. Harlow Ave.
Vancouver, B.C. V6N2K4 Canada
Nice to have
• - For the "FRONT" side of our business card. You can separate or re-arrange with our logo components (icon, logo,slogan). It does not have to be together.

Also our company legal name is rather long so arrange or organize the name in a way to make it shorter. Your experience and creativity will have to come in play.
Should not have
• should not have other colors beside logo color and black text (2 colors). Also nothing Three dimensional

```html
<!DOCTYPE html>
<html lang="en">
<head>
<meta charset="utf-8">
<title>Ferncliff Media – Business Card</title>
<link rel="stylesheet" href="https://fonts.googleapis.com/css2?family=Alegreya:wght@400;500;700&display=swap">
<style>
  :root {
    --brand-blue: #2f8cf7;
    --ink: #0d0d0d;
    --paper: #ffffff;
    --backdrop: #2b2823;
  }
  * { box-sizing: border-box; margin: 0; padding: 0; }
  html, body {
    width: 1200px;
    height: 1200px;
    overflow: hidden;
    background: var(--backdrop);
  }
  body {
    position: relative;
    font-family: "Alegreya", Georgia, serif;
    color: var(--ink);
  }
  .card {
    position: absolute;
    left: 110px;
    width: 980px;
    height: 560px;
    background: var(--paper);
    overflow: hidden;
  }
  .card--front { top: 30px; }
  .card--back { top: 610px; }

  /* Front */
  .front-band {
    position: absolute;
    left: 0; right: 0;
    top: 262px; bottom: 0;
    background: var(--brand-blue);
  }
  .brand-tag {
    position: absolute;
    color: var(--brand-blue);
    font-weight: 700;
    white-space: nowrap;
  }
  .brand-tag--corner-top { left: 24px; top: 22px; font-size: 22px; }
  .company-name {
    position: absolute;
    left: 150px;
    top: 92px;
    font-size: 62px;
    font-weight: 500;
    letter-spacing: 1px;
    line-height: 1;
    white-space: nowrap;
  }
  .company-name__suffix {
    position: absolute;
    right: 140px;
    top: 166px;
    font-size: 42px;
    font-weight: 500;
    letter-spacing: 1px;
    line-height: 1;
  }
  .contact {
    position: absolute;
    right: 22px;
    top: 300px;
    text-align: right;
    font-size: 34px;
    line-height: 1.15;
  }
  .contact__country {
    display: block;
    text-align: center;
    padding-left: 120px;
  }
  .person {
    position: absolute;
    left: 100px;
    top: 420px;
  }
  .person__name { font-size: 38px; font-weight: 700; margin-left: 44px; line-height: 1.1; }
  .person__role { font-size: 27px; line-height: 1.3; }
  .person__email { font-size: 20px; margin-left: 34px; line-height: 1.4; }

  /* Back */
  .site-url {
    position: absolute;
    left: 20px;
    top: 22px;
    font-size: 31px;
    font-weight: 500;
  }
  .back-lockup {
    position: absolute;
    left: 0; right: 0;
    top: 200px;
    text-align: center;
  }
  .back-lockup__name {
    color: var(--brand-blue);
    font-size: 68px;
    font-weight: 700;
    line-height: 1;
  }
  .back-lockup__slogan {
    margin-top: 22px;
    font-size: 30px;
    line-height: 1;
  }
  .brand-tag--corner-bottom { right: 24px; bottom: 22px; font-size: 22px; }
</style>
</head>
<body>
  <section class="card card--front" aria-label="Card front">
    <div class="front-band"></div>
    <div class="brand-tag brand-tag--corner-top">Ferncliff Media</div>
    <h1 class="company-name">TALLPINE&nbsp; FERNCLIFF</h1>
    <div class="company-name__suffix">MEDIA</div>
    <address class="contact" style="font-style:normal">
      Phone: 604 555 0138<br>
      #2217 - 581 E. Harlow<br>
      Ave. Vancouver, B.C. V6N2K4<br>
      <span class="contact__country">CANADA</span>
    </address>
    <div class="person">
      <div class="person__name">Dale Morrow</div>
      <div class="person__role">Director of Sales &amp; Marketing</div>
      <div class="person__email">dale@tallpineferncliff.biz</div>
    </div>
  </section>

  <section class="card card--back" aria-label="Card back">
    <div class="site-url">www.tallpineferncliff.biz</div>
    <div class="back-lockup">
      <div class="back-lockup__name">Ferncliff Media</div>
      <div class="back-lockup__slogan">Your Information Gateway</div>
    </div>
    <div class="brand-tag brand-tag--corner-bottom">Ferncliff Media</div>
  </section>
</body>
</html>
```